Chatterwall and Glimmerly advertising

We need Chatterwall and Glimmerly ads. Simple ad with Alaska themed background.
This ad is to introduce our new KESTREL Internet service.
--Speeds to 500 mpbs
-- Packages start at only $89.99 for speeds to 100mbps
-- Fiber Optic based connection, Not satellite
-- Extreme low latency, consistent speeds
--FREE equipment, FREE Installation, FREE wifi router, First month of service FREE

```html
<!DOCTYPE html>
<html lang="en">
<head>
<meta charset="utf-8">
<title>Northwind Skylink – KESTREL Internet Service</title>
<link href="https://fonts.googleapis.com/css2?family=Montserrat:ital,wght@0,400;0,500;0,700;0,900;1,500;1,600;1,700;1,800&display=swap" rel="stylesheet">
<style>
  :root {
    --sky-deep: #0b56a6;
    --sky-mid: #1478cf;
    --sky-light: #3aa0e8;
    --snow: #cfe6f8;
    --white: #ffffff;
    --ink-blue: #0f5aa8;
    --panel: rgba(80, 150, 225, 0.55);
    --badge: #0e2a45;
  }
  * { margin: 0; padding: 0; box-sizing: border-box; }
  html, body { width: 960px; height: 1200px; overflow: hidden; }
  body { font-family: "Montserrat", sans-serif; color: var(--white); background: var(--sky-deep); }

  .ad {
    position: relative;
    width: 960px;
    height: 1200px;
    overflow: hidden;
    background: linear-gradient(180deg, var(--sky-deep) 0%, var(--sky-mid) 40%, var(--sky-light) 70%, var(--sky-mid) 100%);
  }
  .scene {
    position: absolute; inset: 0;
    background:
      radial-gradient(ellipse 420px 260px at 560px 640px, rgba(207,230,248,0.45), transparent 70%),
      radial-gradient(ellipse 300px 160px at 120px 700px, rgba(255,255,255,0.35), transparent 70%),
      radial-gradient(ellipse 320px 180px at 860px 1080px, rgba(255,255,255,0.35), transparent 70%);
  }
  .person-photo {
    position: absolute;
    left: 40px; top: 535px;
    width: 530px; height: 665px;
    border-radius: 220px 220px 0 0;
    background: linear-gradient(180deg, rgba(196,160,130,0.35) 0%, rgba(190,190,195,0.45) 45%, rgba(230,200,160,0.4) 70%, rgba(150,160,175,0.4) 100%);
  }

  .brand {
    position: absolute; left: 58px; top: 68px;
    display: flex; align-items: center; gap: 10px;
    font-weight: 700; font-size: 25px; letter-spacing: -0.3px;
  }
  .brand-dot { width: 10px; height: 10px; border-radius: 50%; background: var(--white); }

  .product-badge {
    position: absolute; left: 792px; top: 44px;
    width: 118px; height: 62px;
    background: var(--badge);
    display: flex; align-items: center; padding-left: 10px;
    font-weight: 500; font-size: 15px; letter-spacing: 0.5px;
  }

  .headline {
    position: absolute; left: 0; right: 0; top: 196px;
    text-align: center;
    font-weight: 900; font-size: 146px; line-height: 1; letter-spacing: 2px;
  }
  .subhead {
    position: absolute; left: 0; right: 0; top: 362px;
    text-align: center;
    font-weight: 600; font-style: italic; font-size: 38px; letter-spacing: 0.5px;
  }

  .feature { position: absolute; display: flex; align-items: center; gap: 14px; }
  .feature-icon { flex: none; }
  .feature-text { font-weight: 700; font-style: italic; font-size: 22px; line-height: 27px; }
  .feature--speed { left: 456px; top: 508px; }
  .feature--fiber { left: 398px; top: 574px; }
  .feature--latency { left: 466px; top: 682px; }

  .perks { position: absolute; top: 826px; left: 0; width: 960px; }
  .perk { position: absolute; font-weight: 700; font-style: italic; font-size: 22px; white-space: nowrap; }
  .perk:nth-child(1) { left: 593px; top: 0; }
  .perk:nth-child(2) { left: 587px; top: 27px; }
  .perk:nth-child(3) { left: 580px; top: 54px; }
  .perk:nth-child(4) { left: 574px; top: 81px; }

  .packages {
    position: absolute; left: 447px; top: 1033px;
    width: 285px; height: 98px;
    border-radius: 12px;
    background: var(--panel);
  }
  .packages-tab {
    position: absolute; left: 60px; top: -20px;
    width: 166px; height: 39px;
    border-radius: 8px;
    background: var(--white);
    color: var(--ink-blue);
    font-weight: 700; font-style: italic; font-size: 22px;
    display: flex; align-items: center; justify-content: center;
  }
  .packages-col { position: absolute; top: 26px; text-align: left; }
  .packages-col--price { left: 37px; }
  .packages-col--speed { left: 165px; }
  .packages-label { font-weight: 400; font-size: 18px; letter-spacing: 1px; }
  .packages-value { font-weight: 800; font-style: italic; font-size: 33px; line-height: 1.15; }
  .packages-value small { font-size: 14px; font-weight: 500; }
  .packages-divider { position: absolute; left: 142px; top: 52px; width: 2px; height: 37px; background: var(--white); }
</style>
</head>
<body>
<main class="ad">
  <div class="scene" role="img" aria-label="Snow-capped Alaskan mountain peak rising through clouds under a blue sky, with soft wifi signal shapes"></div>
  <div class="person-photo" role="img" aria-label="Excited young man in a grey t-shirt holding a laptop and cheering"></div>

  <div class="brand"><span class="brand-dot"></span>Northwind Skylink</div>
  <div class="product-badge">KESTREL</div>

  <h1 class="headline">KESTREL</h1>
  <p class="subhead">INTERNET SERVICE</p>

  <div class="feature feature--speed">
    <svg class="feature-icon" width="84" height="48" viewBox="0 0 84 48">
      <path d="M6 44 A36 36 0 0 1 78 44" fill="none" stroke="#fff" stroke-width="9" stroke-dasharray="10 4"/>
      <circle cx="42" cy="42" r="5" fill="#fff"/>
      <path d="M42 42 L80 46" stroke="#fff" stroke-width="4" stroke-linecap="round"/>
    </svg>
    <span class="feature-text">Speed Up to 500 mbps</span>
  </div>

  <div class="feature feature--fiber">
    <svg class="feature-icon" width="48" height="86" viewBox="0 0 48 86">
      <path d="M24 0 V14" stroke="#fff" stroke-width="3"/>
      <circle cx="24" cy="20" r="6" fill="none" stroke="#fff" stroke-width="3"/>
      <path d="M6 36 Q24 24 42 36 V60 L46 86 H2 L6 60 Z" fill="#fff"/>
      <g fill="#1478cf"><circle cx="16" cy="44" r="3"/><circle cx="24" cy="42" r="3"/><circle cx="32" cy="44" r="3"/><circle cx="12" cy="53" r="3"/><circle cx="20" cy="52" r="3"/><circle cx="28" cy="52" r="3"/><circle cx="36" cy="53" r="3"/></g>
    </svg>
    <span class="feature-text">Fiber Optic Based Connection,<br>Not Satellite</span>
  </div>

  <div class="feature feature--latency">
    <svg class="feature-icon" width="70" height="70" viewBox="0 0 70 70">
      <path d="M66 4 C46 4 30 14 22 34 L36 48 C56 40 66 24 66 4 Z" fill="#fff"/>
      <circle cx="46" cy="24" r="6" fill="#1478cf"/>
      <path d="M22 34 L8 34 L18 22 L30 22 Z M36 48 L36 62 L48 52 L48 40 Z" fill="#fff"/>
      <path d="M18 44 C8 46 4 56 4 66 C14 66 24 62 26 52 Z" fill="#fff"/>
    </svg>
    <span class="feature-text">Extreme Low Latency,<br>Consistent Speeds</span>
  </div>

  <ul class="perks" style="list-style:none">
    <li class="perk">FREE equipment,</li>
    <li class="perk">FREE Installation</li>
    <li class="perk">FREE wifi router</li>
    <li class="perk">First month of service FREE</li>
  </ul>

  <section class="packages">
    <div class="packages-tab">Packages</div>
    <div class="packages-col packages-col--price">
      <div class="packages-label">start at</div>
      <div class="packages-value">$89<small>.99</small></div>
    </div>
    <div class="packages-divider"></div>
    <div class="packages-col packages-col--speed">
      <div class="packages-label">speeds to</div>
      <div class="packages-value">100<small>mbps</small></div>
    </div>
  </section>
</main>
</body>
</html>
```